KRV Business Cards

We are a local commercial development company based in Silicon Valley and we would like a new business card. I've attached a copy of our company brochure to give a flavor of what we do, our logo, info company colors/graphics, and our current business card. We don't necessarily need a crazy makeover, but would like something that feels a little bit more "fresh" and modern (we've had the same business card design for 15+ years), but still in keeping with our overall brand -- clean, high-quality, modern but timeless. Would like to add our website to the info on the card (www.lumbrel.com) and would like the flexibility for some folks to have an efax number listed and some not to have that included (without it looking like there is a hole).

```html
<!DOCTYPE html>
<html lang="en">
<head>
<meta charset="utf-8">
<title>KRV Development Company – Business Cards</title>
<link rel="stylesheet" href="https://fonts.googleapis.com/css2?family=Open+Sans:wght@400;700&display=swap">
<style>
  :root {
    --page-bg: #e9ebee;
    --navy: #34536f;
    --navy-deep: #2c4761;
    --steel-light: #5f8fbb;
    --paper: #f7f7f6;
    --ink: #5b5f66;
    --white: #ffffff;
  }
  * { box-sizing: border-box; margin: 0; padding: 0; }
  html, body { width: 1200px; height: 900px; overflow: hidden; }
  body {
    background: var(--page-bg);
    font-family: "Open Sans", Arial, sans-serif;
    position: relative;
  }
  .card {
    position: absolute;
    width: 680px;
    height: 388px;
    overflow: hidden;
    box-shadow: 0 10px 28px rgba(0,0,0,.18);
  }

  /* Front */
  .card-front {
    left: 120px; top: 46px;
    background: linear-gradient(60deg, var(--steel-light) 0%, #46709a 35%, var(--navy) 70%, var(--navy-deep) 100%);
  }
  .card-front .wordmark {
    position: absolute;
    left: 50%; top: 150px;
    transform: translateX(-50%);
    color: var(--white);
    font-size: 24px;
    line-height: 1.05;
    letter-spacing: .04em;
    text-transform: uppercase;
    font-weight: 400;
    white-space: nowrap;
  }
  .card-front .website {
    position: absolute;
    left: 40px; bottom: 40px;
    color: var(--white);
    font-size: 15px;
    letter-spacing: .55em;
  }

  /* Back */
  .card-back {
    left: 400px; top: 466px;
    background: var(--paper);
  }
  .card-back .band {
    position: absolute; inset: 0;
    width: 680px; height: 388px;
  }
  .card-back .logo-panel {
    position: absolute;
    left: 40px; top: 48px;
    width: 270px; height: 132px;
    background: var(--navy);
    display: flex; align-items: center; justify-content: center;
  }
  .card-back .logo-panel .wordmark {
    color: var(--white);
    font-size: 20px;
    line-height: 1.08;
    letter-spacing: .04em;
    text-transform: uppercase;
    font-weight: 400;
  }
  .contact {
    position: absolute;
    left: 40px; top: 204px;
    color: var(--ink);
    font-size: 15px;
    line-height: 21px;
  }
  .contact ul { list-style: none; }
  .contact li { display: flex; align-items: center; gap: 12px; }
  .contact svg { width: 15px; height: 15px; fill: var(--ink); flex: none; }
  .person {
    position: absolute;
    right: 30px; top: 116px;
    text-align: right;
    color: var(--white);
  }
  .person .name { font-weight: 700; font-size: 20px; line-height: 1.1; }
  .person .role { font-size: 13px; }
</style>
</head>
<body>

<section class="card card-front" aria-label="Business card front">
  <p class="wordmark">KRV Development<br>Company, LLC</p>
  <p class="website">www.lumbrel.com</p>
</section>

<section class="card card-back" aria-label="Business card back">
  <svg class="band" viewBox="0 0 680 388" aria-hidden="true">
    <polygon points="450,96 680,96 680,388 0,388 0,374 340,374 450,196" fill="var(--navy)"/>
  </svg>

  <div class="logo-panel">
    <p class="wordmark">KRV Development<br>Company, LLC</p>
  </div>

  <address class="contact" style="font-style:normal">
    <p>212 Bramley Avenue</p>
    <p>Los Altos,California 94022</p>
    <ul>
      <li>
        <svg viewBox="0 0 16 16" aria-label="Office"><path d="M2 5c0-2 2-3 6-3s6 1 6 3v1h-3V5H5v1H2zM3 7h10l1 7H2zm5 1.5a2 2 0 1 0 0 4 2 2 0 0 0 0-4z"/></svg>
        650.555.0142
      </li>
      <li>
        <svg viewBox="0 0 16 16" aria-label="Mobile"><path d="M4 1h8v14H4zm1.5 1.5v9h5v-9zM8 12.3a.9.9 0 1 0 0 1.8.9.9 0 0 0 0-1.8z"/></svg>
        650.555.0187
      </li>
      <li>
        <svg viewBox="0 0 16 16" aria-label="Fax"><path d="M4 1h7v4H4zM1 6h14v7H1zm2 2v1h4V8zm0 2v1h4v-1zm9-2v1h1V8zM4 13h8v2H4z"/></svg>
        650.555.0163
      </li>
      <li>
        <svg viewBox="0 0 16 16" aria-label="Email"><path d="M1 3h14v10H1zm1.5 1.5v.4L8 9l5.5-4.1v-.4z"/></svg>
        nora@lumbrel.com
      </li>
    </ul>
  </address>

  <div class="person">
    <p class="name">Nora J. Whitcombe</p>
    <p class="role">Partner</p>
  </div>
</section>

</body>
</html>
```